KAZ Freightworks #ALLKAZ Business Cards & Letterhead

I am looking to business cards designed for our organization. We are currently undergoing a small re-branding that is taking place. Our organization is called KAZ Freightworks and we are headquartered in Phoenix, AZ. We primarily provide transportation and logistics services to the Meridel Parcel Bureau who is our largest customer. I would like to see a design that incorporates name, title, contact info, website, and address (this will be different depending on the employee). I would also like to see some color on the business card using our logo colors or a variation. I would like our logo on the back of the business card with the website displayed. The final design should communicate that we are a next generation transportation operate that focuses on being driver-first, customer-centric, innovative, and sustainable.We would also like our #ALLKAZ catch phrase incorporated as well.
Updates

Decision maker traveling outside of the country until Monday, November 25th.

Target Market(s)

Transportation & Logistics

Industry/Entity Type

Trucking Company

Contact Information for Business Card

-First and Last Name
-Position Title
-Contact Phone
-Contact Email
-Physical Address

Font styles to use
Serif

Colors

Designer to choose colors to be used in the design.

Requirements
Must have
• -KAZ logo prominently displayed
• -#ALLKAZ catch phrase used
• -Some amount of color, design gradient, etc.
• -Logo on the back with website listed (https://www.kazfreightco.example)

```html
<!DOCTYPE html>
<html lang="en">
<head>
<meta charset="utf-8">
<title>KAZ Freightworks Stationery</title>
<link rel="stylesheet" href="https://fonts.googleapis.com/css2?family=Open+Sans:wght@400;600&family=Lato:wght@400;700&display=swap">
<style>
  :root {
    --green: #7dc142;
    --navy: #0d3a46;
    --ink: #4a4a4a;
    --paper: #ffffff;
    --backdrop: #e4e4e4;
  }
  * { box-sizing: border-box; margin: 0; padding: 0; }
  html, body { width: 1200px; height: 1200px; overflow: hidden; }
  body { background: var(--backdrop); position: relative; font-family: "Open Sans", sans-serif; color: var(--ink); }

  .sheet { position: absolute; background: var(--paper); box-shadow: 0 3px 10px rgba(0,0,0,.18); }

  /* Letterhead */
  .letterhead { left: 119px; top: 278px; width: 556px; height: 716px; }
  .letterhead .top-rule { position: absolute; left: 0; top: 0; width: 100%; height: 8px; background: var(--green); }
  .brand-mark {
    position: absolute; border: 2px solid var(--green); border-radius: 50%;
    display: flex; align-items: center; justify-content: center;
    font-family: "Lato", sans-serif; font-weight: 700; color: var(--navy); letter-spacing: 1px;
  }
  .letterhead .brand-mark { left: 243px; top: 17px; width: 74px; height: 74px; font-size: 26px; }

  .letter { position: absolute; left: 52px; top: 128px; width: 450px; font-size: 8.6px; line-height: 11px; }
  .letter p { margin-bottom: 0; }
  .letter .date { margin-bottom: 10px; }
  .letter .recipient { margin-bottom: 29px; }
  .letter .salutation { margin-bottom: 21px; }
  .letter .body p { line-height: 16px; text-align: justify; margin-bottom: 16px; }
  .letter .closing { margin-top: 27px; }
  .signature { display: block; width: 128px; height: 16px; margin: 6px 0 6px; background: linear-gradient(90deg, #d8d8d8, #eeeeee); }
  .signer { font-size: 11px; color: #333; margin-bottom: 3px; }

  .letterhead .address-line { position: absolute; left: 0; top: 911px; }
  .letter-footer-address { position: absolute; left: 0; width: 100%; top: 672px; text-align: center; font-family: "Lato", sans-serif; font-size: 10.5px; color: var(--navy); }
  .letter-footer-address strong { font-weight: 700; }
  .letter-footer-band {
    position: absolute; left: 0; bottom: 0; width: 100%; height: 24px; background: var(--navy);
    font-family: "Lato", sans-serif; font-size: 10.5px; color: #fff;
    display: flex; align-items: center; justify-content: center; gap: 20px;
  }
  .tagline { color: var(--green); }

  /* Envelope front */
  .envelope-front { left: 715px; top: 492px; width: 432px; height: 217px; }
  .envelope-front .top-rule { position: absolute; left: 0; top: 0; width: 100%; height: 6px; background: var(--green); }
  .envelope-front .brand-mark { left: 28px; top: 10px; width: 49px; height: 49px; font-size: 17px; }
  .envelope-band {
    position: absolute; left: 0; bottom: 0; width: 100%; height: 20px; background: var(--navy);
    color: #fff; font-family: "Lato", sans-serif; font-size: 8px; display: flex; align-items: center; justify-content: center;
  }

  /* Envelope back */
  .envelope-back { left: 717px; top: 743px; width: 429px; height: 214px; }
  .envelope-flap { position: absolute; left: 0; top: 0; width: 429px; height: 51px; }
  .envelope-back .flap-name {
    position: absolute; left: 0; top: 9px; width: 100%; text-align: center;
    font-family: "Lato", sans-serif; font-weight: 700; font-size: 27px; color: var(--navy); letter-spacing: 1px;
  }
  .envelope-back .bottom-rule { position: absolute; left: 0; bottom: 0; width: 100%; height: 8px; background: var(--navy); }
</style>
</head>
<body>

<section class="sheet letterhead">
  <div class="top-rule"></div>
  <div class="brand-mark">KAZ</div>

  <div class="letter">
    <p class="date">Issuing Date: May 5, 2018</p>
    <div class="recipient">
      <p>Name Of Employee Mr. XYZABC</p>
      <p>Address of Employee</p>
      <p>Address Line 2 etc..</p>
    </div>
    <p class="salutation">Dear Mr.XYZABC</p>
    <div class="body">
      <p>Lorem Ipsum has been the industry's standard dummy text ever since the 1500s, when an unknown printer took a galley of type and scrambled it to make a type specimen book. It has survived not only five centuries, but also the leap into electronic typesetting, remaining essentially unchanged. It was popularised in the 1960s with the release of Letraset sheets containing Lorem Ipsum passages, and more recently with desktop publishing software like Aldus PageMaker including versions of Lorem Ipsum.</p>
      <p>Lorem Ipsum is simply dummy text of the printing and typesetting industry. Lorem Ipsum has been the industry's standard dummy text ever since the 1500s, when an unknown printer took a galley of type and scrambled it to make a type specimen book.</p>
      <p>It has survived not only five centuries, but also the leap into electronic typesetting, remaining essentially unchanged. It was popularised in the 1960s with the release of Letraset sheets containing Lorem IpsumIpsum passages.</p>
    </div>
    <p class="closing">Yours Sincerely</p>
    <span class="signature" role="img" aria-label="Handwritten signature of Dorian Vell"></span>
    <p class="signer">Dorian Vell</p>
    <p>Managing Director</p>
  </div>

  <p class="letter-footer-address"><strong>KAZ FREIGHTWORKS:</strong> 421, Address line here Country Name, 45452</p>
  <div class="letter-footer-band">
    <span>P: 555-014 273 960 | E: hello@kazfreightco.example | www.kazfreightco.example</span>
    <span class="tagline">#ALLKAZ</span>
  </div>
</section>

<section class="sheet envelope-front">
  <div class="top-rule"></div>
  <div class="brand-mark">KAZ</div>
  <div class="envelope-band">KAZ FREIGHTWORKS: 421, Address line goes here Country Name, 45452</div>
</section>

<section class="sheet envelope-back">
  <svg class="envelope-flap" viewBox="0 0 429 51" aria-hidden="true">
    <polygon points="0,0 429,0 411,51 16,51" fill="var(--green)"/>
  </svg>
  <div class="flap-name">KAZ</div>
  <div class="bottom-rule"></div>
</section>

</body>
</html>
```